Corporate Design für Sanfte Nacht Kinderberatung
Vielen Dank für die tolle und unkomplizierte Zusammenarbeit.
Zielgruppe
Wir informieren, trainieren und coachen Eltern darin, wie sie ihre Babies und Kleinkinder zum Schlafen brinen.
Zielgruppe sind alle Eltern, in der Regel Akademiker, deren 0-3 jährigen Kinder Ein- und/oder Durchschlafprobleme haben
Aufgabenstellung
Ich bräuchte bitte Vorschläge mit 2 verschiedenen Namen, da ich in diesem Jahr heiraten werde:
- mein aktueller Name ist Lena Borwitz
- mein künftiger Name ist Lena Saller
- Eventuell kann das CD meine Initialien im Firmennamen beinhalten, wie z.B.: SAnfte nacht kinderberatung (nur eine Idee, auf die ich allerdings nicht festgelegt bin :-)) Ihr wisst das besser
- ich bräuchte bitte auch einen Header für meine bereits existierende Pagora Domain
- das CD sollte nicht zu verspielt sein und kompetent wirken

```html
<!DOCTYPE html>
<html lang="de">
<head>
<meta charset="utf-8">
<title>Sanfte Nacht Kinderberatung – Visitenkarten</title>
<link href="https://fonts.googleapis.com/css2?family=Baloo+2:wght@800&family=Poppins:wght@400;600&display=swap" rel="stylesheet">
<style>
  :root {
    --backdrop: #2a2a2c;
    --blue-light: #2186d6;
    --blue-deep: #0d5fa8;
    --sky: #d3eafc;
    --orange: #f4b23f;
    --orange-deep: #e09b25;
    --ink: #333333;
    --white: #ffffff;
  }
  * { box-sizing: border-box; margin: 0; padding: 0; }
  html, body {
    width: 1200px; height: 960px; overflow: hidden;
    background: var(--backdrop);
  }
  .sheet {
    width: 1200px; height: 960px;
    display: flex; flex-direction: column; align-items: center; justify-content: center;
    gap: 36px;
  }
  .card {
    position: relative;
    width: 760px; height: 434px;
    overflow: hidden;
    box-shadow: 0 10px 30px rgba(0,0,0,.5);
  }
  .card__bg { position: absolute; inset: 0; width: 100%; height: 100%; }

  /* Front */
  .card--front {
    background: linear-gradient(180deg, var(--blue-light) 0%, var(--blue-deep) 100%);
  }
  .brand {
    position: absolute; left: 90px; top: 130px;
    display: flex; align-items: center; gap: 30px;
  }
  .brand__dot {
    width: 130px; height: 130px; border-radius: 50%;
    background: var(--orange);
    flex: none;
  }
  .brand__text { display: flex; flex-direction: column; }
  .brand__name {
    font-family: "Baloo 2", sans-serif; font-weight: 800;
    color: var(--white);
    font-size: 46px; line-height: 1;
    width: 440px;
  }
  .brand__rule {
    height: 3px; background: var(--orange);
    margin: 12px 0 10px; width: 420px;
  }
  .brand__person {
    font-family: "Poppins", sans-serif; font-weight: 400;
    color: var(--white); font-size: 22px; letter-spacing: .5px;
  }

  /* Back */
  .card--back { background: var(--sky); }
  .contact {
    position: absolute; left: 58px; top: 120px;
    font-family: "Poppins", sans-serif; color: var(--ink);
  }
  .contact__name { font-size: 30px; font-weight: 400; margin-bottom: 40px; }
  .contact__name strong { font-weight: 600; }
  .contact__line { font-size: 16px; line-height: 1.55; }
  .address {
    position: absolute; left: 58px; bottom: 36px;
    font-family: "Poppins", sans-serif; font-size: 16px; color: var(--white);
  }
  .back-brand {
    position: absolute; right: 36px; top: 150px;
    width: 300px; text-align: center;
    display: flex; flex-direction: column; align-items: center; gap: 18px;
  }
  .back-brand .brand__dot { width: 80px; height: 80px; }
  .back-brand .brand__name { font-size: 36px; width: 300px; }
</style>
</head>
<body>
<main class="sheet">

  <section class="card card--front" aria-label="Visitenkarte Vorderseite">
    <div class="brand">
      <span class="brand__dot" aria-hidden="true"></span>
      <div class="brand__text">
        <p class="brand__name">Sanfte Nacht Kinderberatung</p>
        <span class="brand__rule" aria-hidden="true"></span>
        <p class="brand__person">Lena Borwitz</p>
      </div>
    </div>
  </section>

  <section class="card card--back" aria-label="Visitenkarte Rückseite">
    <svg class="card__bg" viewBox="0 0 760 434" preserveAspectRatio="none" aria-hidden="true">
      <defs>
        <linearGradient id="waveBlue" x1="0" y1="0" x2="0" y2="1">
          <stop offset="0" stop-color="#2186d6"/>
          <stop offset="1" stop-color="#0d5fa8"/>
        </linearGradient>
        <linearGradient id="bandOrange" x1="0" y1="0" x2="0" y2="1">
          <stop offset="0" stop-color="#f4b23f"/>
          <stop offset="1" stop-color="#e09b25"/>
        </linearGradient>
      </defs>
      <path d="M0 360 C 160 325, 300 330, 470 342 L 520 434 L 0 434 Z" fill="url(#bandOrange)"/>
      <path d="M430 0 L760 0 L760 434 L520 434 C 470 330, 380 250, 385 140 C 390 70, 410 30, 430 0 Z" fill="url(#waveBlue)"/>
    </svg>
    <div class="contact">
      <p class="contact__name"><strong>Lena</strong> Borwitz</p>
      <p class="contact__line">01234 - 567 890 123</p>
      <p class="contact__line">hallo@sanftenacht-beratung.de</p>
      <p class="contact__line">www.sanftenacht-beratung.de</p>
    </div>
    <p class="address">54321 Beispielstadt, Lindenweg 7</p>
    <div class="back-brand">
      <span class="brand__dot" aria-hidden="true"></span>
      <p class="brand__name">Sanfte Nacht Kinderberatung</p>
    </div>
  </section>

</main>
</body>
</html>
```